Quality Improvement Software for healthcare agencies needs a website.

Veltrix820 is a software for hospices and home health agencies to manage their Quality Assurance Performance Improvement programs to remain complaint with the standards set by Sanovia and the Bureau of Civic Wellbeing. The web accessible software-as-a-service provides an easy, turn-key way for agencies to organize all the information they need to manage and track.

Coded - Design and coding required

4 page

```html
<!DOCTYPE html>
<html lang="en">
<head>
<meta charset="utf-8">
<title>Veltrix820 — Closing The Quality Improvement Loop</title>
<link href="https://fonts.googleapis.com/css2?family=Lexend:wght@400;500;600;700&family=Inter:ital,wght@0,400;0,500;0,600;0,700;1,400&display=swap" rel="stylesheet">
<style>
:root{
  --green:#6ab42d;
  --green-deep:#4fa33a;
  --blue:#2ea8e6;
  --navy:#1c2b4a;
  --orange:#f7931e;
  --ink:#1f1f1f;
  --muted:#777b80;
  --white:#ffffff;
  --black:#000000;
  --card-shadow:0 10px 30px rgba(0,0,0,.10);
}
*{box-sizing:border-box;margin:0;padding:0}
html,body{width:1200px;height:3764px;overflow:hidden}
body{position:relative;background:var(--white);font-family:"Inter",sans-serif;color:var(--ink)}
.abs{position:absolute}
.heading{font-family:"Lexend",sans-serif}
.btn{position:absolute;display:flex;align-items:center;justify-content:center;background:var(--orange);color:var(--white);font-size:15px;font-family:"Inter",sans-serif}

/* header */
.topline{left:0;top:0;width:1200px;height:6px;background:#2a2a2a}
.header{left:0;top:6px;width:1200px;height:70px;background:var(--white)}
.brand{display:flex;align-items:center;gap:9px;font-family:"Lexend",sans-serif;font-weight:600;font-size:28px;color:var(--navy)}
.brand .mark{width:22px;height:22px;background:var(--green)}
.header .brand{position:absolute;left:55px;top:20px}
.nav{position:absolute;top:25px;left:0;font-size:15px;font-weight:500;color:#222}
.nav span{position:absolute;white-space:nowrap}
.nav .active{color:var(--green)}

/* hero */
.hero{left:0;top:76px;width:1200px;height:604px;background:linear-gradient(100deg,#3c4046 0%,#6e7278 40%,#9ea2a6 70%,#b9bcbe 100%)}
.hero-title{left:0;top:200px;width:1196px;text-align:center;color:var(--white);font-size:58px;font-weight:500;line-height:58px;letter-spacing:-1px}
.hero-sub{left:0;top:335px;width:1196px;text-align:center;color:var(--white);font-size:16px;line-height:21px}

.pillar{top:612px;width:310px;height:196px;background:var(--white);box-shadow:var(--card-shadow);text-align:center}
.pillar svg{position:absolute;left:120px;top:30px}
.pillar p{position:absolute;left:0;width:100%;font-family:"Lexend",sans-serif;font-size:21px;line-height:24px;color:var(--ink)}

/* about */
.about-photo{left:127px;top:955px;width:336px;height:336px;border-radius:50%;background:linear-gradient(135deg,#e6f7f6 0%,#a9e3df 50%,#5dc1bd 100%)}
.about-title{left:643px;top:950px;font-size:41px;font-weight:700;color:var(--ink)}
.about-text{left:643px;top:1016px;width:470px;font-size:15px;line-height:22.6px;color:var(--muted)}

/* features */
.features{left:0;top:1386px;width:1200px;height:805px;background:linear-gradient(180deg,#66b62d 0%,#3fb07a 45%,#2ea8e6 100%)}
.features-title{left:0;top:90px;width:1170px;text-align:center;color:var(--white);font-size:41px;font-weight:600;letter-spacing:-1px}
.feat{position:absolute;width:300px;color:var(--white)}
.feat h3{font-family:"Lexend",sans-serif;font-weight:600;font-size:24px;line-height:31px;margin-top:20px}
.feat p{font-size:15.5px;line-height:23px;margin-top:10px}

/* testimonials */
.section-title{left:0;width:1200px;text-align:center;font-size:41px;font-weight:600;color:var(--ink);letter-spacing:-1px}
.quote{left:280px;top:2364px;width:640px;text-align:center;font-style:italic;font-size:20px;line-height:29px;color:var(--muted)}
.avatar{left:521px;top:2476px;width:46px;height:46px;border-radius:50%;background:#c9c2bb}
.client-name{left:586px;top:2481px;font-size:15px;font-weight:600;color:var(--green)}
.client-role{left:586px;top:2505px;font-size:13px;color:var(--muted)}
.dot{top:2545px;width:10px;height:10px;border-radius:50%;background:#dcdcdc}

/* posts */
.post{width:345px;background:var(--white);box-shadow:var(--card-shadow)}
.post .thumb{position:absolute;left:18px;top:18px;width:309px;height:205px}
.post h4{position:absolute;left:37px;width:280px;font-family:"Lexend",sans-serif;font-weight:600;font-size:18px;line-height:20px;color:var(--ink)}
.post .btn{left:37px;width:131px;height:42px}

/* cta */
.cta{left:0;top:3332px;width:1200px;height:123px;background:linear-gradient(90deg,#1e4e7a 0%,#3d7a66 60%,#66b82e 100%)}
.cta-text{left:55px;top:44px;color:var(--white);font-size:27px;font-weight:600;letter-spacing:-.5px}
.cta-btn{position:absolute;left:830px;top:44px;width:138px;height:35px;background:var(--white);border:1px solid #d0d0d0;display:flex;align-items:center;justify-content:center;font-size:14px;color:#2a3b55}

/* footer */
.footer{left:0;top:3455px;width:1200px;height:309px;background:var(--black);color:var(--white)}
.footer .brand{position:absolute;left:55px;top:70px;color:#2d6cb0}
.footer .brand .mark{background:var(--green)}
.footer h5{position:absolute;font-size:16px;font-weight:700}
.footer .links{position:absolute;left:427px;top:122px;font-size:13px;line-height:27.5px}
.social{position:absolute;top:180px;width:25px;height:25px;background:#c8e6b0;border-radius:2px}
.footer .rule{position:absolute;left:40px;top:262px;width:1115px;height:1px;background:#444}
.footer small{position:absolute;font-size:12px}
</style>
</head>
<body>

<div class="abs topline"></div>
<header class="abs header">
  <div class="brand"><span class="mark"></span>Veltrix820</div>
  <nav class="nav">
    <span class="active" style="left:367px">Home</span>
    <span style="left:441px">About</span>
    <span style="left:515px">Products</span>
    <span style="left:610px">Solutions</span>
    <span style="left:709px">Pricing</span>
    <span style="left:791px">Contact</span>
  </nav>
  <div class="btn" style="left:1009px;top:13px;width:134px;height:42px">Free Demo</div>
</header>

<section class="abs hero" role="img" aria-label="Photo of a senior doctor and a younger clinician reviewing records on a laptop in an office">
  <h1 class="abs heading hero-title">Closing The Quality<br>Improvement Loop</h1>
  <p class="abs hero-sub">The web accessible software-as-a-service provides an easy, turn-key way for agencies<br>to organize all the information they need to manage and track.</p>
  <div class="btn" style="left:509px;top:396px;width:175px;height:41px">Request A Demo</div>
</section>

<div class="abs pillar" style="left:104px">
  <svg width="70" height="70" viewBox="0 0 70 70"><defs><linearGradient id="ig" x1="0" y1="0" x2="1" y2="1"><stop offset="0" stop-color="#7cc242"/><stop offset="1" stop-color="#1aa7a8"/></linearGradient></defs><circle cx="35" cy="35" r="35" fill="url(#ig)"/><g fill="none" stroke="#fff" stroke-width="2"><circle cx="35" cy="33" r="13"/><circle cx="35" cy="33" r="6"/><path d="M22 52h26"/></g></svg>
  <p style="top:104px">Maximize Quality<br>And Performance</p>
</div>
<div class="abs pillar" style="left:433px">
  <svg width="70" height="70" viewBox="0 0 70 70"><circle cx="35" cy="35" r="35" fill="url(#ig)"/><g fill="none" stroke="#fff" stroke-width="2"><rect x="19" y="20" width="32" height="22" rx="2"/><path d="M29 48h12M35 42v6M30 31h10M35 26v10"/></g></svg>
  <p style="top:120px">Reduce Burden On<br>Your Care Providers</p>
</div>
<div class="abs pillar" style="left:762px">
  <svg width="70" height="70" viewBox="0 0 70 70"><circle cx="35" cy="35" r="35" fill="url(#ig)"/><g fill="none" stroke="#fff" stroke-width="2"><rect x="23" y="18" width="24" height="34" rx="2"/><path d="M29 27h12M29 33h12M29 39h8M31 16h8v5h-8z"/></g></svg>
  <p style="top:120px">Improve Your<br>Bottom Line</p>
</div>

<div class="abs about-photo" role="img" aria-label="Photo of a clinician using a tablet showing a quality dashboard"></div>
<h2 class="abs heading about-title">Veltrix820</h2>
<p class="abs about-text">Many business owners struggle to understand<br>and maximize the true value of their businesses. This lack of awareness can lead to selling their business for less than it’s worth, poor timing in the market, and inadequate preparation for the complexities of a business sale. They often face challenges in making their business attractive to buyers and aligning the sale with their personal and financial goals. This<br>overall lack of preparedness and insight can result in significant financial and emotional regrets post-sale.</p>
<div class="btn" style="left:643px;top:1253px;width:164px;height:42px">More About US</div>

<section class="abs features" role="img" aria-label="Team meeting photo beneath a green to blue gradient">
  <h2 class="abs heading features-title">Features &amp; Benefits of TrackBoards</h2>

  <div class="feat" style="left:80px;top:218px">
    <svg width="40" height="40" viewBox="0 0 40 40" fill="none" stroke="#fff" stroke-width="2"><ellipse cx="20" cy="9" rx="17" ry="6"/><path d="M3 9v22c0 3.3 7.6 6 17 6s17-2.7 17-6V9M3 16c0 3.3 7.6 6 17 6s17-2.7 17-6M3 24c0 3.3 7.6 6 17 6s17-2.7 17-6"/></svg>
    <h3>Centralize Quality<br>Program Data</h3>
    <p>Ut elit tellus, luctus nec ullamcorper<br>mattis, pulvinar dapibus leo.</p>
  </div>
  <div class="feat" style="left:452px;top:218px">
    <svg width="40" height="40" viewBox="0 0 40 40" fill="none" stroke="#fff" stroke-width="2"><circle cx="20" cy="23" r="15"/><path d="M16 3h8M20 3v5M20 23l6-7M33 10l3-3"/></svg>
    <h3>Spend Less Time On<br>Compliance</h3>
    <p>Ut elit tellus, luctus nec ullamcorper<br>mattis, pulvinar dapibus leo.</p>
  </div>
  <div class="feat" style="left:821px;top:218px">
    <svg width="44" height="40" viewBox="0 0 44 40" fill="none" stroke="#fff" stroke-width="2"><circle cx="22" cy="8" r="6"/><path d="M2 20l8-4 8 4 6-3 6 3 8-4 4 2M10 18l-6 10M34 18l6 10M14 26l8 8 8-8M18 24l8 8"/></svg>
    <h3>Reduce The Cost Of<br>Compliance</h3>
    <p>Ut elit tellus, luctus nec ullamcorper<br>mattis, pulvinar dapibus leo.</p>
  </div>

  <div class="feat" style="left:80px;top:477px">
    <svg width="44" height="40" viewBox="0 0 44 40" fill="none" stroke="#fff" stroke-width="2"><circle cx="22" cy="8" r="6"/><path d="M12 26c0-6 4.5-10 10-10s10 4 10 10M4 38h36M8 38v-8h8v8M28 38v-8h8v8"/></svg>
    <h3>Improve Performance<br>And Star Rating</h3>
    <p>Ut elit tellus, luctus nec ullamcorper<br>mattis, pulvinar dapibus leo.</p>
  </div>
  <div class="feat" style="left:452px;top:477px">
    <svg width="40" height="40" viewBox="0 0 40 40" fill="none" stroke="#fff" stroke-width="2"><rect x="7" y="5" width="26" height="30"/><path d="M7 12h26M12 18h4M19 18h9M12 24h4M19 24h9M12 30h4M19 30h9"/></svg>
    <h3>Eliminate Paper Forms<br>And Binders</h3>
    <p>Ut elit tellus, luctus nec ullamcorper<br>mattis, pulvinar dapibus leo.</p>
  </div>
  <div class="feat" style="left:821px;top:477px">
    <svg width="40" height="40" viewBox="0 0 40 40" fill="none" stroke="#fff" stroke-width="2"><rect x="8" y="17" width="24" height="20" rx="2"/><path d="M13 17v-6a7 7 0 0 1 14 0v6M20 24v6"/></svg>
    <h3>Data Security And<br>Privacy</h3>
    <p>Ut elit tellus, luctus nec ullamcorper<br>mattis, pulvinar dapibus leo.</p>
  </div>
</section>

<h2 class="abs heading section-title" style="top:2264px">What Client Says</h2>
<p class="abs quote">Gravida penatibus viverra dis litora quam eget malesuada mus est enim sed tortor dignissim hendrerit aliquet pharetra habitant blandit</p>
<div class="abs avatar" role="img" aria-label="Client portrait"></div>
<span class="abs client-name">Marten Holloway</span>
<span class="abs client-role">Enterpreneur</span>
<span class="abs dot" style="left:571px;background:var(--green)"></span>
<span class="abs dot" style="left:591px"></span>
<span class="abs dot" style="left:612px"></span>

<h2 class="abs heading section-title" style="top:2707px">Latest Posts</h2>

<article class="abs post" style="left:50px;top:2777px;height:421px">
  <div class="thumb" role="img" aria-label="Photo of three colleagues working together at a laptop" style="background:linear-gradient(135deg,#dfe3e8,#b7bcc4)"></div>
  <h4 style="top:282px">Electronic Health or Medical Records</h4>
  <div class="btn" style="top:341px">Learn more</div>
</article>
<article class="abs post" style="left:424px;top:2777px;height:439px">
  <div class="thumb" role="img" aria-label="Photo of a clinician using a tablet with a management dashboard" style="background:linear-gradient(135deg,#e4f6f5,#8fd3cf)"></div>
  <h4 style="top:280px">5 Must-Haves in a Hospital Information Management System</h4>
  <div class="btn" style="top:359px">Learn more</div>
</article>
<article class="abs post" style="left:800px;top:2777px;height:421px">
  <div class="thumb" role="img" aria-label="Photo of a group of colleagues discussing documents" style="background:linear-gradient(135deg,#d9d6d2,#9a958f)"></div>
  <h4 style="top:282px">5 Steps To Making A Successful Career Pivot In Your Fifties</h4>
  <div class="btn" style="top:361px">Learn more</div>
</article>

<section class="abs cta">
  <p class="abs heading cta-text">Are You Ready? Claim Your Free Account Now.</p>
  <div class="cta-btn">SIGNUP NOW</div>
</section>

<footer class="abs footer">
  <div class="brand"><span class="mark"></span>Veltrix820</div>
  <p class="abs" style="left:55px;top:129px;font-size:15px">Closing The Quality Improvement Loop</p>
  <span class="social" style="left:55px"></span>
  <span class="social" style="left:88px"></span>
  <span class="social" style="left:121px"></span>
  <span class="social" style="left:154px"></span>

  <h5 style="left:427px;top:62px">Quick Links</h5>
  <div class="links">Home<br>About<br>Services<br>Solutions</div>

  <h5 style="left:798px;top:62px">Get in Touch</h5>
  <p class="abs" style="left:798px;top:110px;font-size:14.5px;line-height:22px">Jln Melati Raya No 14<br>Bandung - Indonesia</p>
  <svg class="abs" style="left:798px;top:178px" width="16" height="12" viewBox="0 0 16 12" fill="none" stroke="#6ab42d" stroke-width="1.4"><rect x="1" y="1" width="14" height="10"/><path d="M1 1l7 6 7-6"/></svg>
  <p class="abs" style="left:824px;top:173px;font-size:14.5px">support@veltrix820.example</p>
  <svg class="abs" style="left:798px;top:205px" width="16" height="16" viewBox="0 0 16 16" fill="none" stroke="#6ab42d" stroke-width="1.4"><path d="M3 1l3 3-2 2c1 2 4 5 6 6l2-2 3 3-2 2C7 15 1 9 1 3z"/></svg>
  <p class="abs" style="left:824px;top:203px;font-size:14.5px">+123 9876 543</p>

  <div class="rule"></div>
  <small style="left:49px;top:293px">Copyright © Veltrix820 TrackBoard. All rights reserved.</small>
  <small style="left:880px;top:293px">Term of use <span style="color:var(--green)">•</span> Privacy Policy <span style="color:var(--green)">•</span> Cookie Policy</small>
</footer>

</body>
</html>
```